Round Label Sticker 2.5-3 inch diameter

We need a design for a sticker to distribute for more brand recognition and product outreach.
My company The Bright Kettle Company Ltd. Specializes in working with people with diabetes. My products are made for diabetics because they have no added sugars, high in protein and fiber and each serving is lower than 5% daily value of carbohydrates.
I am a dietitian and my dad passed away from diabetes. I have created a growing food and beverage line that will give more joy into a diabetic's life while providing more food options that make them feel happy instead of guilty when they eat it.
I am teaching cooking classes to promote my products as well as doing exhibits and events. I want to give away a sticker to people that reads "I'm too sweet for sugar!" and somewhere on it would be my logo as well as my website info. www.brightkettle.example
The sticker should make people smile and warm as well as draw interest to my product line.
Target Market(s)
Diabetes and people who do not want added sugars in their food
Industry/Entity Type
Food Store
Requirements
Must have
- my logo and website

```html
<!DOCTYPE html>
<html lang="en">
<head>
<meta charset="utf-8">
<title>Bright Kettle – I'm too sweet for sugar sticker</title>
<link rel="stylesheet" href="https://fonts.googleapis.com/css2?family=Gochi+Hand&family=PT+Sans:wght@700&display=swap">
<style>
  :root {
    --purple: #5b2a86;
    --cream: #ede7cf;
    --paper: #ffffff;
    --green-light: #8dc63f;
    --green-dark: #3a9a46;
    --green-text: #3f9a3c;
  }
  html, body {
    margin: 0;
    padding: 0;
    width: 1000px;
    height: 1200px;
    overflow: hidden;
    background: var(--paper);
  }
  .sticker {
    display: block;
    width: 1000px;
    height: 1200px;
  }
  .sticker__edge { fill: var(--cream); stroke: var(--purple); stroke-width: 16; }
  .sticker__face { fill: var(--cream); }
  .brand-name {
    font-family: "PT Sans", sans-serif;
    font-weight: 700;
    font-size: 48px;
    fill: var(--purple);
    letter-spacing: 3px;
  }
  .brand-dot { fill: var(--green-text); }
  .slogan {
    font-family: "Gochi Hand", cursive;
    font-size: 165px;
    fill: var(--purple);
    stroke: var(--paper);
    stroke-width: 8px;
    stroke-linejoin: round;
    paint-order: stroke fill;
  }
  .website {
    font-family: "PT Sans", sans-serif;
    font-weight: 700;
    font-size: 36px;
    fill: var(--green-text);
  }
</style>
</head>
<body>
<svg class="sticker" viewBox="0 0 1000 1200" xmlns="http://www.w3.org/2000/svg">
  <defs>
    <linearGradient id="band-tone" x1="0" y1="0" x2="1" y2="1">
      <stop offset="0" stop-color="#8dc63f"/>
      <stop offset="0.5" stop-color="#5fb046"/>
      <stop offset="1" stop-color="#3a9a46"/>
    </linearGradient>
    <path id="website-arc" d="M 282 912 Q 500 905 735 868"/>
  </defs>

  <circle class="sticker__edge" cx="513" cy="607" r="478"/>

  <circle cx="513" cy="607" r="458" fill="url(#band-tone)" role="img" aria-label="Twisted candy-stripe ring in light and dark green"/>

  <circle class="sticker__face" cx="513" cy="607" r="395"/>

  <g class="brand">
    <circle class="brand-dot" cx="372" cy="350" r="11"/>
    <text class="brand-name" x="523" y="366" text-anchor="middle">Bright Kettle</text>
  </g>

  <text class="slogan" x="510" y="585" text-anchor="middle" textLength="670" lengthAdjust="spacingAndGlyphs">I'm too sweet</text>
  <text class="slogan" x="503" y="790" text-anchor="middle" textLength="430" lengthAdjust="spacingAndGlyphs">for sugar</text>

  <text class="website"><textPath href="#website-arc" textLength="450" lengthAdjust="spacingAndGlyphs">www.brightkettle.example</textPath></text>
</svg>
</body>
</html>
```